Book cover required for new book business book (Otter Ambush SEO for Managed Service Providers)

We are finalizing publishing dates for our latest business book. The audience this book is targetting is IT business owners. Demographic age 30-50 years of age, male, middle class. The title of the book is Otter Ambush SEO for managed service providers. The author name is Dean Harrow. The book goes into details about how to improve SEO for IT businesses. The premise of the book is if a bear attacked a crowd of people, and you were in that crowd, you'd only have to be 1% faster to outrun the bear. The same is true for your IT Businesses website. You only have to put in 1% more effort into your SEO to be on page one of Zarvio.
We have been using a working draft image whilst the book has been in preproduction. I am unsure if this working image is licensed. Please find attached.

```html
<!DOCTYPE html>
<html lang="en">
<head>
<meta charset="utf-8">
<title>Otter Ambush SEO for Managed Service Providers — Cover</title>
<link rel="stylesheet" href="https://fonts.googleapis.com/css2?family=Oswald:wght@400;500&display=swap">
<style>
  :root {
    --ink-black: #000000;
    --sand: #d7a865;
    --paper: #ffffff;
    --fur-light: #efe2c8;
    --fur-warm: #d9a364;
    --rock: #6e5a4c;
    --water: #b9a79f;
  }
  * { margin: 0; padding: 0; box-sizing: border-box; }
  html, body {
    width: 675px; height: 1200px; overflow: hidden;
    background: var(--ink-black);
  }
  .cover {
    position: relative; width: 675px; height: 1200px;
    background: var(--ink-black);
    font-family: "Oswald", "Arial Narrow", sans-serif;
    color: var(--paper);
  }
  .title-panel {
    position: absolute; left: 0; top: 123px; width: 347px; height: 774px;
    background: var(--sand);
  }
  .publisher-mark {
    position: absolute; left: 0; top: 123px; width: 114px; height: 101px;
    background: var(--paper);
    display: flex; flex-direction: column; align-items: center; justify-content: center; gap: 6px;
    color: var(--sand);
  }
  .publisher-mark .dot {
    width: 40px; height: 40px; border: 2px solid var(--sand); border-radius: 50%;
  }
  .publisher-mark .name {
    font-size: 13px; font-weight: 400; letter-spacing: 1px; text-transform: uppercase; line-height: 1;
  }
  .book-title {
    position: absolute; left: 81px; top: 255px; width: 262px;
    font-size: 64px; font-weight: 400; line-height: 86px;
    text-transform: uppercase; letter-spacing: 0;
  }
  .book-title span { display: block; white-space: nowrap; }
  .tagline {
    position: absolute; left: 98px; top: 869px; width: 249px;
    font-size: 22px; font-weight: 400; line-height: 1; white-space: nowrap;
    text-transform: uppercase; letter-spacing: -0.3px;
  }
  .blank-band {
    position: absolute; left: 0; top: 897px; width: 347px; height: 150px;
    background: var(--paper);
    display: flex; align-items: center; padding-left: 81px;
  }
  .author {
    font-size: 30px; font-weight: 400; line-height: 1;
    text-transform: uppercase; letter-spacing: 1px;
    color: var(--sand);
  }
  .base-strip {
    position: absolute; left: 0; top: 1047px; width: 347px; height: 29px;
    background: var(--sand);
  }
  .cover-photo {
    position: absolute; left: 347px; top: 123px; width: 328px; height: 953px;
    background:
      radial-gradient(ellipse 75% 55% at 70% 62%, var(--fur-light) 0%, var(--fur-warm) 55%, transparent 80%),
      linear-gradient(160deg, var(--water) 0%, var(--water) 30%, var(--rock) 60%, #4b3d33 100%);
  }
</style>
</head>
<body>
  <div class="cover">
    <div class="title-panel"></div>
    <div class="publisher-mark">
      <span class="dot"></span>
      <span class="name">Kelpmark</span>
    </div>
    <h1 class="book-title">
      <span>Otter</span>
      <span>Ambush</span>
      <span>SEO for</span>
      <span>Managed</span>
      <span>Service</span>
      <span>Providers</span>
    </h1>
    <p class="tagline">Improve CEO for IT business</p>
    <div class="blank-band">
      <p class="author">Dean Harrow</p>
    </div>
    <div class="base-strip"></div>
    <div class="cover-photo" role="img" aria-label="Photograph of a cream and tan polar bear lifting its head, resting against dark rocks beside water"></div>
  </div>
</body>
</html>
```